Business cards and Stationary for Bright Learning Alliance
A Chinese Education Consulting Company
Business cards and Stationary for Bright Learning Alliance - Education
Creative Brief
Professional
Dennis R. Tolwy
Manager
7214 Marlow Court, San Ramon, CA 94583
dennistolwy@brilearnal.com
www.brilearnal.com
Please leave abundant space for multi address, (2) multi cell phones (3)

```html
<!DOCTYPE html>
<html lang="en">
<head>
<meta charset="utf-8">
<title>Bright Learning Alliance – Stationery</title>
<link href="https://fonts.googleapis.com/css2?family=Cinzel:wght@700&family=Open+Sans:wght@400;600&display=swap" rel="stylesheet">
<style>
:root{
  --bg:#1b1b1b;
  --red:#c4101b;
  --red-dark:#7e0008;
  --red-light:#e0262d;
  --gold:#d8b25a;
  --paper:#ffffff;
  --paper-shade:#eeeeee;
  --ink:#333333;
  --faint:#f1e3e3;
  --caption:#bbbbbb;
}
*{margin:0;padding:0;box-sizing:border-box}
html,body{width:1200px;height:353px;overflow:hidden;background:var(--bg)}
body{position:relative;font-family:"Open Sans",Arial,sans-serif;color:var(--ink)}
.piece{position:absolute;overflow:hidden;box-shadow:0 2px 6px rgba(0,0,0,.6)}
.white{background:var(--paper)}
.red{background:radial-gradient(circle at 50% 40%,var(--red-light),var(--red) 55%,var(--red-dark))}
.brand{position:absolute;left:50%;transform:translateX(-50%);display:flex;align-items:center;gap:3px;white-space:nowrap;font-family:"Cinzel",serif;font-weight:700;color:var(--red)}
.brand .dot{display:block;border-radius:50%;background:var(--gold)}
.red .brand{color:var(--gold)}
.crest-faint{position:absolute;left:50%;transform:translateX(-50%);border-radius:50%;background:radial-gradient(circle,var(--faint),rgba(241,227,227,0) 70%)}
.red .crest-faint{background:radial-gradient(circle,rgba(255,255,255,.12),rgba(255,255,255,0) 70%)}
.band{position:absolute;left:0;right:0;background:linear-gradient(var(--red-light),var(--red-dark))}
.small{font-size:4px;line-height:5.5px}
.caption{position:absolute;font-size:4.5px;color:var(--caption);text-align:center}
.url{position:absolute;color:#fff;font-size:6px}
</style>
</head>
<body>

<!-- business cards -->
<section class="piece white" style="left:19px;top:43px;width:125px;height:101px">
  <div class="brand" style="top:10px;left:28px;transform:none;font-size:6px"><span class="dot" style="width:8px;height:8px"></span></div>
  <div class="small" style="position:absolute;left:44px;top:8px">
    <strong>Dennis R. Tolwy</strong><br>Manager<br><br>7214 Marlow Court<br>San Ramon, CA 94583<br>dennistolwy@brilearnal.com<br>www.brilearnal.com
  </div>
  <div class="crest-faint" style="top:40px;width:60px;height:60px" role="img" aria-label="Faint crest decoration"></div>
  <div class="band" style="bottom:0;height:9px"></div>
</section>

<section class="piece red" style="left:19px;top:156px;width:125px;height:96px">
  <div class="crest-faint" style="top:12px;width:70px;height:70px" role="img" aria-label="Faint crest decoration"></div>
  <div class="brand" style="top:34px;font-size:7px"><span class="dot" style="width:10px;height:10px"></span>Bright Learning Alliance</div>
  <div class="url" style="left:0;right:0;top:76px;text-align:center;font-size:5px">www.brilearnal.com</div>
</section>

<section class="piece white" style="left:19px;top:259px;width:125px;height:77px">
  <div class="band" style="top:0;height:6px"></div>
  <div class="brand" style="top:20px;font-size:6px"><span class="dot" style="width:8px;height:8px"></span>Bright Learning Alliance</div>
  <div class="band" style="bottom:0;height:6px"></div>
</section>

<!-- letterheads -->
<section class="piece white" style="left:168px;top:41px;width:211px;height:295px">
  <div class="brand" style="top:8px;font-size:6px"><span class="dot" style="width:12px;height:12px"></span>Bright Learning Alliance</div>
  <div class="crest-faint" style="top:90px;width:120px;height:110px" role="img" aria-label="Faint crest decoration"></div>
  <div class="band" style="bottom:0;height:10px"></div>
</section>
<div class="caption" style="left:168px;top:338px;width:211px">Letterhead option 1</div>

<section class="piece white" style="left:396px;top:41px;width:216px;height:295px">
  <div class="brand" style="top:8px;font-size:6px"><span class="dot" style="width:12px;height:12px"></span>Bright Learning Alliance</div>
  <div class="crest-faint" style="top:90px;width:120px;height:110px" role="img" aria-label="Faint crest decoration"></div>
  <div class="band" style="bottom:0;height:10px"></div>
</section>
<div class="caption" style="left:396px;top:338px;width:216px">Letterhead option 2</div>

<!-- folder -->
<section class="piece red" style="left:631px;top:41px;width:204px;height:266px">
  <div class="url" style="left:14px;top:90px;font-size:7px">www.brilearnal.com</div>
  <div class="crest-faint" style="top:120px;width:110px;height:110px" role="img" aria-label="Faint crest decoration"></div>
</section>
<section class="piece white" style="left:835px;top:41px;width:197px;height:266px">
  <div class="brand" style="top:10px;font-size:6px"><span class="dot" style="width:12px;height:12px"></span>Bright Learning Alliance</div>
  <div class="crest-faint" style="top:110px;width:110px;height:110px" role="img" aria-label="Faint crest decoration"></div>
</section>
<section class="piece white" style="left:631px;top:264px;width:200px;height:72px;background:linear-gradient(var(--paper),var(--paper-shade))">
  <div class="brand" style="top:20px;font-size:6px"><span class="dot" style="width:12px;height:12px"></span>Bright Learning Alliance</div>
  <div class="band" style="bottom:0;height:6px"></div>
</section>
<section class="piece white" style="left:835px;top:264px;width:197px;height:72px;background:linear-gradient(var(--paper),var(--paper-shade))">
  <div class="brand" style="top:20px;font-size:6px"><span class="dot" style="width:12px;height:12px"></span>Bright Learning Alliance</div>
  <div class="band" style="bottom:0;height:6px"></div>
</section>
<div class="caption" style="left:631px;top:338px;width:400px">Folder</div>

<!-- envelopes -->
<section class="piece white" style="left:1056px;top:24px;width:139px;height:84px">
  <div class="band" style="top:0;height:16px"></div>
  <div class="url" style="left:30px;top:5px;font-size:4.5px">www.brilearnal.com</div>
  <svg style="position:absolute;left:0;top:16px" width="139" height="30"><polygon points="0,0 139,0 69.5,28" fill="#f4f4f4" stroke="#dddddd" stroke-width=".5"/></svg>
</section>
<section class="piece" style="left:1056px;top:120px;width:139px;height:96px;background:linear-gradient(160deg,#f3dd9a,var(--gold) 60%,#a8843a)">
  <svg style="position:absolute;left:0;top:0" width="139" height="40"><polygon points="0,0 139,0 69.5,36" fill="#e9c978" stroke="#b8924a" stroke-width=".5"/></svg>
</section>
<section class="piece white" style="left:1056px;top:228px;width:139px;height:108px">
  <div class="brand" style="top:8px;left:8px;transform:none;font-size:4.5px"><span class="dot" style="width:7px;height:7px"></span>Bright Learning Alliance</div>
  <div style="position:absolute;left:30px;top:48px;width:78px;height:20px;border:1px solid #dddddd"></div>
  <div class="band" style="bottom:0;height:6px"></div>
</section>
<div class="caption" style="left:1056px;top:338px;width:139px">Envelope with window</div>

</body>
</html>
```